Graphic Design Needed for Powerpoint Deck

We need a powerpoint design template, font, and look and feel for a new company called Brookvale Care. Specific needs are listed in the attached file and if we like what we see we will more than likely use you in the future.
We like warm natural colors from a branding point of view, greens, browns, etc.
Target Market(s)
This will be used with potential investors and business partners.
Industry/Entity Type
Graphic Design
Requirements
Must have
- Graphic Designs for the charts mentioned in the powerpoint
- Overall Look and Feel
Nice to have
- Custom Font recommendations (Trebuchet is the one we like the most that is standard)

```html
<!DOCTYPE html>
<html lang="en">
<head>
<meta charset="utf-8">
<title>Brookvale Care – Deck Template</title>
<link href="https://fonts.googleapis.com/css2?family=Ubuntu:wght@400;500;700&display=swap" rel="stylesheet">
<style>
  :root {
    --green-deep: #2e9a2f;
    --green-main: #6cbb24;
    --green-bright: #8fcf3a;
    --green-lime: #a8d81b;
    --green-title: #7cc023;
    --green-text: #43a735;
    --cream: #eef6cf;
    --ink: #2b2b2b;
    --white: #ffffff;
    --sand: #e8c88a;
  }
  * { margin: 0; padding: 0; box-sizing: border-box; }
  html, body {
    width: 1200px; height: 918px; overflow: hidden;
    background: var(--white);
    font-family: "Ubuntu", "Trebuchet MS", sans-serif;
  }
  .canvas { position: relative; width: 1200px; height: 918px; }
  .slide {
    position: absolute; width: 580px; height: 434px; overflow: hidden;
    background: var(--cream);
  }
  .slide--cover { left: 0; top: 0; background: linear-gradient(160deg, var(--green-main), var(--green-bright) 60%, var(--green-main)); }
  .slide--team { left: 620px; top: 0; }
  .slide--press { left: 0; top: 484px; }
  .slide--problem { left: 620px; top: 484px; }
  .slide svg.backdrop { position: absolute; inset: 0; width: 580px; height: 434px; }

  .cover-headline {
    position: absolute; top: 40px; left: 0; width: 580px; text-align: center;
    color: var(--white); font-weight: 700; font-size: 30px; line-height: 30px;
  }
  .cover-headline small { display: block; font-size: 15px; line-height: 18px; margin-top: 1px; }
  .brand-badge {
    position: absolute; left: 203px; top: 142px; width: 174px; height: 174px;
    border-radius: 50%; background: var(--white);
    display: flex; align-items: center; justify-content: center; text-align: center;
    color: #5a5a5a; font-weight: 500; font-size: 15px; line-height: 19px;
  }

  .slide-title {
    position: absolute; left: 40px; color: var(--green-title);
    font-weight: 700; font-size: 29px;
  }
  .title-rule {
    position: absolute; left: 40px; width: 502px; height: 2px; background: var(--green-title);
  }
  .title-rule::after {
    content: ""; position: absolute; right: -16px; top: -7px; width: 16px; height: 16px;
    background: var(--green-title);
  }
  .slide-body {
    position: absolute; left: 40px; color: var(--ink);
    font-size: 13.5px; line-height: 16.8px;
  }
  .slide--team .slide-title { top: 76px; }
  .slide--team .title-rule { top: 120px; }
  .slide--team .slide-body { top: 177px; }
  .slide--team .gap { height: 16.8px; }

  .slide--problem .slide-title { top: 122px; }
  .slide--problem .title-rule { top: 164px; }
  .slide--problem .slide-body { top: 216px; line-height: 21px; }

  .press-note {
    position: absolute; left: 0; top: 160px; width: 580px; text-align: center;
    color: var(--green-text); font-weight: 500; font-size: 34px; line-height: 42px;
  }
</style>
</head>
<body>
<main class="canvas">

  <!-- Cover -->
  <section class="slide slide--cover">
    <svg class="backdrop" viewBox="0 0 580 434" aria-hidden="true">
      <circle cx="290" cy="250" r="270" fill="none" stroke="#ffffff" stroke-opacity="0.22" stroke-width="10"/>
      <circle cx="290" cy="250" r="222" fill="none" stroke="#ffffff" stroke-opacity="0.25" stroke-width="5"/>
      <path d="M73,218 H508 A217.5,217.5 0 0 1 73,218 Z" fill="#ffffff" fill-opacity="0.2"/>
    </svg>
    <h1 class="cover-headline">We aren’t here to<br>present a business model,<small>we’re here to present the future of healthcare</small></h1>
    <div class="brand-badge">BROOKVALE<br>CARE CENTER</div>
  </section>

  <!-- Who are we -->
  <section class="slide slide--team">
    <svg class="backdrop" viewBox="0 0 580 434" aria-hidden="true">
      <circle cx="330" cy="250" r="210" fill="none" stroke="#ffffff" stroke-opacity="0.6" stroke-width="10"/>
      <path d="M0,398 C210,402 420,372 580,300 L580,434 L0,434 Z" fill="var(--green-title)"/>
      <path d="M0,384 C220,380 420,340 580,268 L580,302 C420,372 210,402 0,400 Z" fill="var(--green-deep)"/>
      <path d="M0,372 C220,364 420,318 580,250 L580,264 C420,334 220,372 0,384 Z" fill="var(--green-lime)"/>
    </svg>
    <h2 class="slide-title">Who Are We</h2>
    <div class="title-rule"></div>
    <div class="slide-body">
      Content will be 2 people’s bios<div class="gap"></div>
      WANT TO INTEGRATE THE FOLLOWING LOGOS/THEMES<br>
      Education<br>
      Hollis Military Academy<br>
      Ashford Executive Education<br>
      Corporate<br>
      Meridian Household Goods<br>
      Crestline Stores<br>
      Norvane Consumer Health
    </div>
  </section>

  <!-- Press clippings -->
  <section class="slide slide--press">
    <svg class="backdrop" viewBox="0 0 580 434" aria-hidden="true">
      <rect width="580" height="434" fill="var(--green-main)"/>
      <path d="M0,190 C40,90 140,10 330,8 C480,6 590,60 580,160 L580,434 L0,434 Z" fill="var(--cream)"/>
    </svg>
    <div role="img" aria-label="Faint leaf and ring emblem decoration" style="position:absolute;left:90px;top:40px;width:420px;height:380px;border-radius:50%;background:radial-gradient(circle at 50% 50%, rgba(180,214,120,0.45), rgba(238,246,207,0) 70%);"></div>
    <p class="press-note">Content will be<br>4-5 Article Clippings<br>Need good layout</p>
  </section>

  <!-- The problem -->
  <section class="slide slide--problem">
    <svg class="backdrop" viewBox="0 0 580 434" aria-hidden="true">
      <circle cx="330" cy="230" r="200" fill="none" stroke="#ffffff" stroke-opacity="0.6" stroke-width="10"/>
      <path d="M0,0 H580 V6 C400,20 200,40 0,60 Z" fill="var(--green-title)"/>
      <path d="M0,60 C200,40 400,20 580,6 V26 C400,40 200,62 0,82 Z" fill="var(--green-deep)"/>
      <path d="M0,94 C200,74 400,52 580,40 V50 C400,62 200,84 0,104 Z" fill="var(--green-lime)"/>
      <path d="M0,420 C220,420 420,400 580,356 L580,434 L0,434 Z" fill="var(--green-title)"/>
      <path d="M0,410 C220,408 420,380 580,330 L580,358 C420,402 220,422 0,422 Z" fill="var(--green-deep)"/>
      <path d="M0,400 C220,396 420,366 580,318 L580,328 C420,378 220,406 0,410 Z" fill="var(--green-lime)"/>
    </svg>
    <h2 class="slide-title">The problem</h2>
    <div class="title-rule"></div>
    <div class="slide-body">
      Need data visuals/infographics for the following facts:<br>
      Patients<br>
      Prevention is broadly overlooked today<br>
      One-third of Americans who have diabetes don’t know it<br>
      50% of men and 64% of women who died suddenly of a heart attack, never<br>
      knew they had cardiovascular disease<br>
      66.3% of Americans are overweight
    </div>
  </section>

</main>
</body>
</html>
```